RedField - Rebranding, Namecard, Stationary and One Page Web

Refresh logo, make it modern and design matching name card, stationary and one page web

RedField Information Technology (Int'l) Company Limited
紅原訊息科技(國際)有限公司

Company is System Integrator, and will be providing products and services to government and enterprise organizations. Our Chief Security Officer came from top U.S. vendor, and had been working on top enterprise and government projects globally, so we want the refreshed image of the new company to have a East Cost U.S. style, with hint of technology from Silicon Valley. The company will also be representing top brands from the U.S. on information security.

Branding refresh is needed because company is being acquired and is expanding

Target Market(s)

Cyber Security

Industry/Entity Type

Information Technology

Contact Information for Business Card

Need Chinese and English

Number of Pages Required

1 page

Font styles to use
Sans Serif

Colors
0292cd
00a990

Requirements
Must have
• Modern, clean, cyber look. Must keep same colors and general look and feel of original logo. Only modernization, do not change its personality

```html
<!DOCTYPE html>
<html lang="en">
<head>
<meta charset="utf-8">
<title>RedField Name Card</title>
<link rel="stylesheet" href="https://fonts.googleapis.com/css2?family=Open+Sans:wght@400;600;700&family=Noto+Sans+TC:wght@400&display=swap">
<style>
  :root {
    --page-bg: #ece9e4;
    --card-white: #ffffff;
    --band-blue: #badcec;
    --band-mint: #b5e3d9;
    --brand-blue: #0292cd;
    --brand-teal: #00a990;
    --back-teal: #14ab91;
    --text-dark: #3d3d3d;
    --divider: #7fd0c2;
  }
  * { box-sizing: border-box; margin: 0; padding: 0; }
  html, body { width: 1200px; height: 1200px; overflow: hidden; }
  body {
    background: var(--page-bg);
    font-family: "Open Sans", sans-serif;
    display: flex;
    flex-direction: column;
    align-items: center;
    justify-content: center;
    gap: 60px;
  }
  .card {
    position: relative;
    width: 840px;
    height: 480px;
    overflow: hidden;
    box-shadow: 0 6px 18px rgba(0,0,0,0.12);
  }
  .card-front { background: var(--card-white); }
  .front-bands { position: absolute; inset: 0; }
  .front-logo {
    position: absolute;
    left: 150px;
    top: 330px;
    display: flex;
    align-items: center;
    gap: 14px;
  }
  .logo-dot {
    width: 34px; height: 34px;
    border-radius: 50%;
    background: var(--brand-teal);
  }
  .logo-name {
    font-weight: 700;
    font-size: 44px;
    color: var(--brand-blue);
    letter-spacing: 1px;
  }
  .contact {
    position: absolute;
    left: 470px;
    top: 62px;
    color: var(--text-dark);
    font-size: 17px;
    line-height: 1.5;
  }
  .contact-group {
    border-left: 2px solid var(--divider);
    padding-left: 16px;
    margin-bottom: 18px;
  }
  .person-name {
    font-weight: 700;
    font-size: 30px;
    color: var(--brand-teal);
    letter-spacing: 0.5px;
    line-height: 1.2;
  }
  .person-title {
    font-size: 15px;
    font-weight: 400;
    color: var(--text-dark);
    margin-left: 8px;
  }
  .card-back {
    background: var(--back-teal);
    display: flex;
    flex-direction: column;
    align-items: center;
    justify-content: center;
    color: var(--card-white);
    text-align: center;
  }
  .back-logo {
    display: flex;
    align-items: center;
    gap: 16px;
    margin-bottom: 34px;
  }
  .back-logo .logo-dot { background: var(--card-white); width: 40px; height: 40px; }
  .back-logo .logo-name { color: var(--card-white); font-size: 60px; }
  .company-zh {
    font-family: "Noto Sans TC", sans-serif;
    font-size: 24px;
    letter-spacing: 2px;
    margin-bottom: 8px;
  }
  .company-en { font-size: 19px; }
</style>
</head>
<body>

  <section class="card card-front">
    <svg class="front-bands" width="840" height="480" viewBox="0 0 840 480" aria-hidden="true">
      <rect width="840" height="480" fill="var(--band-blue)"/>
      <ellipse cx="820" cy="500" rx="760" ry="620" fill="var(--card-white)"/>
      <ellipse cx="820" cy="500" rx="745" ry="605" fill="var(--band-mint)"/>
      <ellipse cx="860" cy="520" rx="690" ry="560" fill="var(--card-white)"/>
    </svg>

    <div class="front-logo">
      <span class="logo-dot"></span>
      <span class="logo-name">RedField</span>
    </div>

    <div class="contact">
      <div class="contact-group">
        <div class="person-name">DANIEL LAU<span class="person-title">CEO</span></div>
      </div>
      <div class="contact-group">
        <div>(852) 6120 4817</div>
        <div>www.hkredfield.com.hk</div>
        <div>daniellau@hkredfield.com.hk</div>
      </div>
      <div class="contact-group">
        <div>Office</div>
        <div>Room B, Unit 402, 4/F, Fung Lee</div>
        <div>Ind. Bldg, No 15 Sheung Yuet Road</div>
        <div>Kowloon Bay, Kowloon, HKSAR</div>
      </div>
    </div>
  </section>

  <section class="card card-back">
    <div class="back-logo">
      <span class="logo-dot"></span>
      <span class="logo-name">RedField</span>
    </div>
    <p class="company-zh">紅原訊息科技(國際)有限公司</p>
    <p class="company-en">RedField Information Technology (Int'l) Company Limited</p>
  </section>

</body>
</html>
```